Business card for Northland's Blue Wagon.

Good day i am looking for a business card design for my business.
The name of the business is Northland's Blue Wagon. It is a van rental business that provides a driver and helper to the customer. Customer have use to van for small moves, studio or 1 bedroom, Moving furniture like couch or kitchen cabinets.
We are available evenings, weekends and holidays.
the means to contact us is by phone at 628-947-2071; By emails at Oakridge@northlandsbluewagon.net; or by social media, Facebook and Instagram.
You can see attached pictures of the van and or logo.

```html
<!DOCTYPE html>
<html lang="en">
<head>
<meta charset="utf-8">
<title>Northland's Blue Wagon – Business Card</title>
<link href="https://fonts.googleapis.com/css2?family=Oswald:wght@500;600&family=Poppins:wght@500;600&family=Roboto+Condensed:wght@400;500&display=swap" rel="stylesheet">
<style>
  :root {
    --page: #dcdcdc;
    --card-dark: #0e0e0e;
    --card-mid: #262626;
    --red: #e0101a;
    --red-deep: #b5050c;
    --white: #ffffff;
    --grey-text: #e6e6e6;
  }
  * { margin: 0; padding: 0; box-sizing: border-box; }
  html, body { width: 908px; height: 1200px; overflow: hidden; background: var(--page); }
  .canvas { position: relative; width: 908px; height: 1200px; }

  .card {
    position: absolute;
    left: 74px;
    width: 760px;
    height: 435px;
    overflow: hidden;
    background: radial-gradient(ellipse at 50% 35%, var(--card-mid) 0%, var(--card-dark) 75%);
  }
  .card--front { top: 137px; }
  .card--back { top: 628px; }

  /* Front */
  .brand-mark {
    position: absolute;
    left: 190px; top: 110px; width: 380px;
    text-align: center;
    font-family: "Poppins", sans-serif;
    font-weight: 600;
    font-size: 44px;
    line-height: 1.15;
    color: var(--white);
  }
  .web-pill {
    position: absolute;
    left: 91px; top: 343px; width: 578px; height: 46px;
    border: 2px solid var(--red);
    border-radius: 23px;
    display: flex; align-items: center; justify-content: center;
    font-family: "Poppins", sans-serif;
    font-weight: 600;
    font-size: 22px;
    letter-spacing: 4.2px;
    color: var(--white);
  }
  .web-pill .web-name { color: var(--red); }

  /* Back */
  .brand-mark--small {
    position: absolute;
    left: 22px; top: 52px; width: 165px;
    text-align: center;
    font-family: "Poppins", sans-serif;
    font-weight: 600;
    font-size: 24px;
    line-height: 1.15;
    color: var(--white);
  }
  .availability-frame { position: absolute; left: 0; top: 0; }
  .availability-title {
    position: absolute;
    left: 271px; top: 49px;
    font-family: "Oswald", sans-serif;
    font-weight: 600;
    font-size: 21px;
    letter-spacing: 5.5px;
    color: var(--grey-text);
  }
  .availability-item {
    position: absolute; top: 94px;
    display: flex; align-items: center; gap: 12px;
  }
  .availability-item .icon-ring {
    width: 54px; height: 54px; border-radius: 50%;
    background: var(--white);
    border: 4px solid var(--red);
    box-shadow: 0 0 0 2px #000, 0 0 0 3px var(--red);
    display: flex; align-items: center; justify-content: center;
  }
  .availability-item .label {
    font-family: "Oswald", sans-serif;
    font-weight: 500;
    font-size: 17px;
    letter-spacing: 0.6px;
    color: var(--grey-text);
  }
  .item-evenings { left: 265px; }
  .item-weekends { left: 426px; }
  .item-holidays { left: 589px; }

  .red-band {
    position: absolute;
    left: 0; top: 189px; width: 760px; height: 214px;
    background: linear-gradient(90deg, rgba(224,16,26,0) 0%, var(--red-deep) 30%, var(--red) 60%, var(--red-deep) 100%);
  }
  .van-photo {
    position: absolute;
    left: 0; top: 186px; width: 386px; height: 249px;
    background: linear-gradient(160deg, #d3151c 0%, #a80c12 55%, #3a3a3a 85%, #1a1a1a 100%);
    clip-path: polygon(0 8%, 62% 0, 80% 30%, 100% 62%, 100% 88%, 86% 100%, 0 100%);
  }
  .contact {
    position: absolute; left: 405px; top: 208px; width: 330px;
    color: var(--white);
  }
  .contact .person-name {
    font-family: "Oswald", sans-serif;
    font-weight: 600;
    font-size: 31px;
    line-height: 1;
    letter-spacing: 0.3px;
  }
  .contact .person-role {
    margin-top: 4px;
    font-family: "Poppins", sans-serif;
    font-weight: 500;
    font-size: 17px;
    letter-spacing: 5px;
  }
  .contact .divider {
    margin-top: 9px; height: 1px; width: 323px;
    background: rgba(255,255,255,0.55);
  }
  .contact-line {
    display: flex; align-items: center; gap: 5px;
    font-family: "Roboto Condensed", sans-serif;
    font-size: 20px;
  }
  .contact-line--phone { margin-top: 10px; }
  .contact-line--email { margin-top: 6px; }
  .contact-line .dot {
    width: 19px; height: 19px; border-radius: 50%;
    background: #111;
    display: flex; align-items: center; justify-content: center;
    flex: none;
  }
  .social {
    position: absolute; left: 410px; top: 362px;
    display: flex; align-items: center; gap: 8px;
    font-family: "Poppins", sans-serif;
    font-weight: 600;
    font-size: 15px;
    color: var(--white);
  }
  .social .social-dot {
    width: 19px; height: 19px; border-radius: 50%;
    background: #111;
    border: 1px solid rgba(255,255,255,0.6);
  }
  .social .social-dot:first-of-type { margin-left: 4px; }
</style>
</head>
<body>
<main class="canvas">

  <section class="card card--front" aria-label="Card front">
    <div class="brand-mark">Northland's Blue Wagon</div>
    <div class="web-pill">www.<span class="web-name">NorthlandsBlueWagon</span>.com</div>
  </section>

  <section class="card card--back" aria-label="Card back">
    <div class="brand-mark--small">Northland's Blue Wagon</div>

    <svg class="availability-frame" width="760" height="200" viewBox="0 0 760 200" aria-hidden="true">
      <path d="M500 63 H675 A55 56 0 0 1 675 175 H156" fill="none" stroke="#e0101a" stroke-width="2"/>
    </svg>
    <div class="availability-title">WE ARE AVAILABLE</div>

    <div class="availability-item item-evenings">
      <div class="icon-ring">
        <svg width="28" height="28" viewBox="0 0 28 28" aria-hidden="true">
          <circle cx="16" cy="16" r="9" fill="none" stroke="#111" stroke-width="2.4"/>
          <path d="M16 16 V9 A7 7 0 1 1 9 16 Z" fill="#111"/>
          <rect x="14" y="3" width="4" height="3" fill="#111"/>
          <path d="M2 13 H6 M1 17 H6 M3 21 H7" stroke="#111" stroke-width="2"/>
        </svg>
      </div>
      <span class="label">Evenings</span>
    </div>

    <div class="availability-item item-weekends">
      <div class="icon-ring">
        <svg width="26" height="26" viewBox="0 0 26 26" aria-hidden="true">
          <rect x="3" y="5" width="20" height="18" rx="2" fill="#111"/>
          <rect x="7" y="2" width="2.5" height="5" fill="#111"/>
          <rect x="16.5" y="2" width="2.5" height="5" fill="#111"/>
          <g fill="#fff">
            <rect x="6" y="11" width="3" height="2.5"/><rect x="11.5" y="11" width="3" height="2.5"/><rect x="17" y="11" width="3" height="2.5"/>
            <rect x="6" y="15" width="3" height="2.5"/><rect x="11.5" y="15" width="3" height="2.5"/><rect x="17" y="15" width="3" height="2.5"/>
            <rect x="6" y="19" width="3" height="2"/><rect x="11.5" y="19" width="3" height="2"/><rect x="17" y="19" width="3" height="2"/>
          </g>
        </svg>
      </div>
      <span class="label">Weekends</span>
    </div>

    <div class="availability-item item-holidays">
      <div class="icon-ring">
        <svg width="26" height="26" viewBox="0 0 26 26" aria-hidden="true">
          <rect x="3" y="5" width="20" height="18" rx="2" fill="#111"/>
          <rect x="7" y="2" width="2.5" height="5" fill="#111"/>
          <rect x="16.5" y="2" width="2.5" height="5" fill="#111"/>
          <rect x="5" y="10" width="16" height="11" fill="#111"/>
          <path d="M13 11.5 L14.4 14.5 L17.5 14.8 L15.1 16.8 L15.9 19.8 L13 18.2 L10.1 19.8 L10.9 16.8 L8.5 14.8 L11.6 14.5 Z" fill="#fff"/>
        </svg>
      </div>
      <span class="label">Holidays</span>
    </div>

    <div class="red-band"></div>
    <div class="van-photo" role="img" aria-label="Photo of the red company cargo van with branded side lettering"></div>

    <div class="contact">
      <div class="person-name">ELISE R. TAMBOR</div>
      <div class="person-role">DIRECTOR</div>
      <div class="divider"></div>
      <div class="contact-line contact-line--phone">
        <span class="dot">
          <svg width="11" height="11" viewBox="0 0 24 24" aria-hidden="true"><path fill="#e0101a" d="M6.6 10.8a15.1 15.1 0 0 0 6.6 6.6l2.2-2.2a1 1 0 0 1 1-.25 11.4 11.4 0 0 0 3.6.57 1 1 0 0 1 1 1V20a1 1 0 0 1-1 1A17 17 0 0 1 3 4a1 1 0 0 1 1-1h3.5a1 1 0 0 1 1 1c0 1.25.2 2.45.57 3.57a1 1 0 0 1-.25 1z"/></svg>
        </span>
        628-947-2071
      </div>
      <div class="contact-line contact-line--email">
        <span class="dot">
          <svg width="11" height="11" viewBox="0 0 24 24" aria-hidden="true"><rect x="2" y="5" width="20" height="14" rx="2" fill="#e0101a"/><path d="M3 6 L12 13 L21 6" fill="none" stroke="#111" stroke-width="2"/></svg>
        </span>
        Oakridge@northlandsbluewagon.net
      </div>
    </div>

    <div class="social">
      Follow us on
      <span class="social-dot"></span>
      <span class="social-dot"></span>
      <span class="social-dot"></span>
    </div>
  </section>

</main>
</body>
</html>
```